Packaging Design - Mailer Box for Canadian Gift Box Company

We are a new gift box company in Canada selling only Canadian products. We need a design for a mailer box that will be very unique and noticeable. We would like it to be very Canadian. It can be many colors.
I would like to close the mailer box with a sticker that could perhaps have our logo.
"Gifts from Canada's Best" to be included on the box.
We will be ordering at least 2 sizes so I'd like the artwork to be transferable to other box sizes
I will add a JPG file to my brief that I really love. I found it online but have not purchased it so do not have rights to use it.
Can anyone do something like this on the box design?
Industry/Entity Type
It Company
Colors
Designer to choose colors to be used in the design.
Look and feel

```html
<!DOCTYPE html>
<html lang="en">
<head>
<meta charset="utf-8">
<title>Mailer Box Dielines – Birch &amp; Harbour</title>
<link rel="stylesheet" href="https://fonts.googleapis.com/css2?family=PT+Sans:wght@400;700&display=swap">
<style>
  :root {
    --box-red: #e63a2e;
    --crease: #d8332a;
    --cut-line: #cfcfcf;
    --glue-flap: #e4e4e4;
    --hatch: #b8b8b8;
    --ink: #111111;
    --paper: #ffffff;
  }
  html, body {
    margin: 0;
    padding: 0;
    width: 1200px;
    height: 1181px;
    overflow: hidden;
    background: var(--paper);
  }
  .sheet { display: block; width: 1200px; height: 1181px; }
  .panel { fill: var(--box-red); }
  .cut { fill: var(--paper); stroke: var(--cut-line); stroke-width: 2; }
  .glue { fill: url(#glue-hatch); stroke: var(--cut-line); stroke-width: 2; }
  .crease { stroke: var(--crease); stroke-width: 1; fill: none; }
  .slot { fill: var(--paper); stroke: var(--cut-line); stroke-width: 1.5; }
  .product-icons { fill: #dc372c; stroke: none; }
  .tagline { font-family: "PT Sans", sans-serif; font-weight: 700; fill: var(--ink); }
  .brand-name { font-family: "PT Sans", sans-serif; font-weight: 700; fill: var(--ink); }
  .size-label { font-family: "PT Sans", sans-serif; font-weight: 400; fill: var(--ink); }
</style>
</head>
<body>
<svg class="sheet" viewBox="0 0 1500 1476" xmlns="http://www.w3.org/2000/svg">
  <defs>
    <pattern id="glue-hatch" width="8" height="8" patternUnits="userSpaceOnUse" patternTransform="rotate(45)">
      <rect width="8" height="8" fill="#ececec"/>
      <line x1="0" y1="0" x2="0" y2="8" stroke="#b8b8b8" stroke-width="1.2"/>
    </pattern>
  </defs>

  <!-- Briefcase box -->
  <g class="box box-briefcase">
    <rect class="glue" x="118" y="272" width="120" height="90"/>
    <rect class="glue" x="546" y="272" width="120" height="90"/>
    <rect class="glue" x="118" y="608" width="120" height="92"/>
    <rect class="glue" x="546" y="608" width="120" height="92"/>
    <rect class="cut" x="36" y="367" width="714" height="240"/>
    <path class="cut" d="M150 716 L240 704 L544 704 L634 716 L634 896 Q634 920 610 926 L540 940 L240 940 L172 926 Q148 920 148 896 Z"/>
    <path class="cut" d="M152 958 Q152 948 162 948 L626 948 Q634 948 632 958 L632 985 Q600 1040 550 1040 L236 1040 Q182 1040 152 985 Z"/>
    <rect class="cut" x="240" y="274" width="306" height="94"/>

    <rect class="panel" x="244" y="279" width="297" height="90"/>
    <rect class="panel" x="42" y="372" width="700" height="230"/>
    <rect class="panel" x="244" y="600" width="297" height="106"/>
    <path class="panel" d="M154 720 L244 710 L540 710 L630 720 L630 894 Q630 914 612 920 L540 936 L244 936 L172 920 Q154 914 154 894 Z"/>
    <path class="panel" d="M158 960 Q158 953 165 953 L624 953 Q628 953 628 960 L628 984 Q598 1034 548 1034 L238 1034 Q188 1034 158 984 Z"/>

    <line class="crease" x1="136" y1="372" x2="136" y2="602"/>
    <line class="crease" x1="234" y1="372" x2="234" y2="602"/>
    <line class="crease" x1="552" y1="372" x2="552" y2="602"/>
    <line class="crease" x1="650" y1="372" x2="650" y2="602"/>
    <line class="crease" x1="244" y1="367" x2="541" y2="367"/>
    <line class="crease" x1="244" y1="606" x2="541" y2="606"/>
    <line class="crease" x1="244" y1="706" x2="541" y2="706"/>
    <line class="crease" x1="244" y1="946" x2="541" y2="946"/>
    <line class="crease" x1="240" y1="712" x2="240" y2="936"/>
    <line class="crease" x1="546" y1="712" x2="546" y2="936"/>
    <line class="crease" x1="236" y1="955" x2="236" y2="1034"/>
    <line class="crease" x1="548" y1="955" x2="548" y2="1034"/>

    <rect class="slot" x="228" y="408" width="19" height="48"/>
    <rect class="slot" x="228" y="519" width="19" height="48"/>
    <rect class="slot" x="537" y="408" width="19" height="48"/>
    <rect class="slot" x="537" y="519" width="19" height="48"/>

    <rect class="product-icons" x="158" y="396" width="52" height="172" rx="4" role="img" aria-label="Column of small line icons of gift products: bottle, jar, candle, tube and lotion bottle"/>
    <rect class="product-icons" x="580" y="392" width="56" height="176" rx="4" role="img" aria-label="Column of small line icons of gift products: bottle, jar, candle, tube and lotion bottle"/>

    <text class="tagline" x="393" y="323" font-size="17" text-anchor="middle" transform="rotate(180 393 317)">Give True North Joy</text>
    <text class="brand-name" x="392" y="846" font-size="46" text-anchor="middle">Birch &amp; Harbour</text>
    <text class="tagline" x="392" y="998" font-size="17" text-anchor="middle">Give True North Joy</text>
  </g>

  <!-- Trunk box -->
  <g class="box box-trunk">
    <rect class="glue" x="908" y="313" width="90" height="96"/>
    <rect class="glue" x="1230" y="313" width="90" height="96"/>
    <rect class="glue" x="908" y="588" width="90" height="96"/>
    <rect class="glue" x="1230" y="588" width="90" height="96"/>
    <rect class="cut" x="796" y="408" width="638" height="180"/>
    <path class="cut" d="M910 706 L1005 686 L1225 686 L1318 706 L1318 832 L1225 862 L1005 862 L910 832 Z"/>
    <path class="cut" d="M912 882 Q912 871 922 871 L1308 871 Q1318 871 1316 882 Q1300 958 1232 960 L994 960 Q928 958 912 882 Z"/>
    <rect class="cut" x="998" y="316" width="232" height="92"/>

    <rect class="panel" x="1003" y="320" width="222" height="88"/>
    <rect class="panel" x="802" y="413" width="624" height="170"/>
    <rect class="panel" x="1003" y="580" width="222" height="108"/>
    <path class="panel" d="M916 708 L1005 692 L1225 692 L1312 708 L1312 828 L1225 856 L1005 856 L916 828 Z"/>
    <path class="panel" d="M918 884 Q918 876 926 876 L1304 876 Q1312 876 1310 884 Q1296 952 1232 954 L996 954 Q934 952 918 884 Z"/>

    <line class="crease" x1="893" y1="413" x2="893" y2="583"/>
    <line class="crease" x1="991" y1="413" x2="991" y2="583"/>
    <line class="crease" x1="1237" y1="413" x2="1237" y2="583"/>
    <line class="crease" x1="1336" y1="413" x2="1336" y2="583"/>
    <line class="crease" x1="1003" y1="406" x2="1225" y2="406"/>
    <line class="crease" x1="1003" y1="586" x2="1225" y2="586"/>
    <line class="crease" x1="1003" y1="686" x2="1225" y2="686"/>
    <line class="crease" x1="1003" y1="866" x2="1225" y2="866"/>
    <line class="crease" x1="1005" y1="692" x2="1005" y2="856"/>
    <line class="crease" x1="1225" y1="692" x2="1225" y2="856"/>
    <line class="crease" x1="994" y1="878" x2="994" y2="954"/>
    <line class="crease" x1="1234" y1="878" x2="1234" y2="954"/>

    <rect class="slot" x="986" y="462" width="22" height="70" rx="11"/>
    <rect class="slot" x="1220" y="462" width="22" height="70" rx="11"/>

    <rect class="product-icons" x="922" y="424" width="46" height="148" rx="4" role="img" aria-label="Column of small line icons of gift products: bottle, jar, candle, tube and lotion bottle"/>
    <rect class="product-icons" x="1260" y="424" width="46" height="148" rx="4" role="img" aria-label="Column of small line icons of gift products: bottle, jar, candle, tube and lotion bottle"/>

    <text class="tagline" x="1114" y="364" font-size="16" text-anchor="middle" transform="rotate(180 1114 358)">Give True North Joy</text>
    <text class="brand-name" x="1114" y="792" font-size="36" text-anchor="middle">Birch &amp; Harbour</text>
    <text class="tagline" x="1114" y="918" font-size="16" text-anchor="middle">Give True North Joy</text>
  </g>

  <text class="size-label" x="403" y="1195" font-size="26" text-anchor="middle">Briefcase(12.5x10x4)</text>
  <text class="size-label" x="1114" y="1183" font-size="26" text-anchor="middle">Trunk(9.5x7.75x4</text>
</svg>
</body>
</html>
```